Display Home Banner PWL

Design a Display Home Banner to go on Fence at Display Home.

Banner will need to display company logo and name.

Prefer the entire banner to be approx 6m in length and approx 1.2m high

Must also have the words "Display Home"

Specialising in unique custom built homes, knock down and rebuild

The rest is up to you to give me some ideas of your own. It needs to be modern and elegant in design. We are show casing our industry leading construction work and want to draw peoples attention to the display home!

**** FURTHER UPDATE ********

Just clarifying that I am looking for a long narrow banner (not poster format)

6 metres long and 1.2 metres high .....

Doesn't have to have construction symbols on it .... can be symbols or shapes or colors or images that compliment the text etc .....

Want the building company logo to be more prominent than the words display home but want it to be clear that its a display home banner ....

I am looking for a slick crisp font .... not too blocky or playful .....

don't want reds, yellows, orange colours ......

looking for tranquil, warm soft colours and colors from the logo ....

I am looking for a very professional corporate banner .....

I will update brief and upload logo and files tonight. Sorry for the delay

Reason: Hi Sorry I have been working on another project with another company and this was left on the side. I have now finished building the display home and need the banner for exhibitions in the coming weeks. The banner needs to display the company logo and name as well as the words "Display Home" I have uploaded the logo files for you to use with your designs. It will be approximately 6m in length and the rest of the design I leave open to your creative side :) Any questions please let me know Thanks

Im not sure that the brief was read correctly by everyone?? I am look for a long narrow banner - 6 metres long and 1.2 metres high ...... (Not Poster format) I want to use peaceful tranquil colors and the colors in our logo ..... (Not Red, Yellow and Orange ..... soft warm colours please) I want a modern striking text like the one in the logo ..... Doesn't necessarily have to have construction symbols in the banner .... can just be shapes or symbols or even just areas defined by colors .... has to look corporate and modern with a professional industry leading look to it ..... Hope this helps ! :) Looking forward to seeing some updated concepts! :) Thanks!

Target Market(s)

People looking for a quality builder to build for them.

Industry/Entity Type

Construction

```html
<!DOCTYPE html>
<html lang="en">
<head>
<meta charset="UTF-8">
<title>PWL Display Homes Banner</title>
<link rel="stylesheet" href="https://fonts.googleapis.com/css2?family=Josefin+Sans:wght@700&family=Open+Sans:wght@700&display=swap">
<style>
  :root {
    --page-bg: #ededed;
    --brand-purple: #5e4f9e;
    --accent-mauve: #a47a9c;
    --floral-pink: #d98fb1;
    --floral-rose: #c95a86;
    --text-white: #ffffff;
  }
  html, body {
    margin: 0;
    padding: 0;
    width: 1200px;
    height: 1000px;
    overflow: hidden;
    background: radial-gradient(ellipse at center, #f7f7f7 0%, var(--page-bg) 70%, #dcdcdc 100%);
  }
  .canvas {
    position: relative;
    width: 1200px;
    height: 1000px;
  }
  .banner {
    position: absolute;
    left: 0;
    top: 380px;
    width: 1200px;
    height: 240px;
    display: flex;
  }
  .banner__floral {
    width: 265px;
    height: 100%;
    background:
      radial-gradient(circle at 10% 75%, var(--floral-rose) 0%, rgba(201,90,134,0) 35%),
      radial-gradient(circle at 45% 90%, var(--floral-pink) 0%, rgba(217,143,177,0) 45%),
      linear-gradient(160deg, var(--brand-purple) 20%, #8a6fb3 100%);
  }
  .banner__message {
    width: 595px;
    height: 100%;
    background: var(--accent-mauve);
    display: flex;
    flex-direction: column;
    align-items: center;
    color: var(--text-white);
  }
  .location-pin {
    margin-top: 30px;
    width: 56px;
    height: 79px;
  }
  .banner__title {
    margin: 14px 0 0;
    font-family: "Josefin Sans", sans-serif;
    font-weight: 700;
    font-size: 38px;
    letter-spacing: 3px;
    line-height: 1;
  }
  .banner__tagline {
    margin: 10px 0 0;
    font-family: "Open Sans", sans-serif;
    font-weight: 700;
    font-size: 11.5px;
    letter-spacing: 0.2px;
    text-transform: uppercase;
  }
  .banner__brand {
    flex: 1;
    height: 100%;
    background: var(--brand-purple);
    display: flex;
    align-items: center;
    justify-content: center;
    gap: 16px;
  }
  .brand-square {
    width: 26px;
    height: 26px;
    background: var(--text-white);
  }
  .brand-name {
    font-family: "Josefin Sans", sans-serif;
    font-weight: 700;
    font-size: 84px;
    letter-spacing: 8px;
    color: var(--text-white);
    line-height: 1;
    padding-top: 12px;
  }
</style>
</head>
<body>
<div class="canvas">
  <section class="banner">
    <div class="banner__floral" role="img" aria-label="Illustration of soft pink and lilac flower petals and leaves"></div>
    <div class="banner__message">
      <svg class="location-pin" viewBox="0 0 58 82" aria-hidden="true">
        <path d="M29 2 C13 2 2 14 2 29 C2 46 20 62 29 80 C38 62 56 46 56 29 C56 14 45 2 29 2 Z" fill="#ffffff"/>
        <circle cx="29" cy="29" r="17" fill="#a47a9c"/>
        <path d="M19 33 L29 23 L39 33 M23 30 V37 H35 V30" fill="none" stroke="#ffffff" stroke-width="2.5" stroke-linejoin="round"/>
      </svg>
      <h1 class="banner__title">DISPLAY HOMES</h1>
      <p class="banner__tagline">Specialising in unique custom built homes, knock down and rebuild</p>
    </div>
    <div class="banner__brand">
      <span class="brand-square" aria-hidden="true"></span>
      <span class="brand-name">PWL</span>
    </div>
  </section>
</div>
</body>
</html>
```